Brightwave Business Card

Professional Business Card Design required using the attached contact information.

Contact information can be rearranged as required.

The company is a new start up venture developing solar systems, the branding should be in keeping with that of one of the investors whose website is as follows https://www.quorvex.com/

```html
<!DOCTYPE html>
<html lang="en">
<head>
<meta charset="UTF-8">
<title>Brightwave Renewables – Business Card</title>
<link href="https://fonts.googleapis.com/css2?family=Advent+Pro:wght@300;400;600&display=swap" rel="stylesheet">
<style>
  :root {
    --stage: #1f2a3b;
    --card-light: #ffffff;
    --card-dark: #1e2a3c;
    --ink: #111418;
    --green: #3aa64a;
    --muted: #56667a;
  }
  * { margin: 0; padding: 0; box-sizing: border-box; }
  html, body {
    width: 1000px; height: 1200px; overflow: hidden;
    background: var(--stage);
    font-family: "Advent Pro", sans-serif;
  }
  .card {
    position: absolute;
    left: 178px;
    width: 645px;
    height: 430px;
  }
  .card--front {
    top: 145px;
    background: var(--card-light);
  }
  .card--back {
    top: 625px;
    background: var(--card-dark);
    box-shadow: 0 20px 60px rgba(0, 0, 0, 0.35);
  }
  .wordmark {
    position: absolute;
    left: 0; right: 0; top: 192px;
    display: flex; align-items: center; justify-content: center; gap: 12px;
    color: var(--ink);
    font-weight: 600;
    font-size: 34px;
    letter-spacing: 0.5px;
    line-height: 1;
  }
  .wordmark__dot {
    width: 12px; height: 12px; border-radius: 50%;
    background: var(--ink);
  }
  .holder__name {
    position: absolute;
    left: 55px; top: 76px;
    color: var(--green);
    font-weight: 400;
    font-size: 52px;
    letter-spacing: 2px;
    line-height: 1;
  }
  .holder__title {
    position: absolute;
    left: 55px; top: 124px;
    color: var(--muted);
    font-weight: 400;
    font-size: 19px;
    line-height: 1;
  }
  .contacts {
    position: absolute;
    left: 44px; top: 265px;
    list-style: none;
    color: var(--muted);
    font-weight: 300;
    font-size: 23px;
    line-height: 1.2;
  }
  .contacts__item {
    display: flex; align-items: flex-start; gap: 17px;
    margin-bottom: 6px;
  }
  .contacts__icon {
    width: 20px; height: 20px; flex: none; margin-top: 4px;
    fill: var(--muted);
  }
</style>
</head>
<body>
  <section class="card card--front">
    <div class="wordmark">
      <span>BRIGHTWAVE RENEWABLES</span>
      <span class="wordmark__dot"></span>
    </div>
  </section>

  <section class="card card--back">
    <h1 class="holder__name">DANIEL MERROW</h1>
    <p class="holder__title">Founder/CEO</p>
    <ul class="contacts">
      <li class="contacts__item">
        <svg class="contacts__icon" viewBox="0 0 24 24" aria-hidden="true"><path d="M6.6 10.8c1.4 2.8 3.8 5.1 6.6 6.6l2.2-2.2c.3-.3.7-.4 1-.2 1.1.4 2.3.6 3.6.6.6 0 1 .4 1 1V20c0 .6-.4 1-1 1C10.6 21 3 13.4 3 4c0-.6.4-1 1-1h3.5c.6 0 1 .4 1 1 0 1.3.2 2.5.6 3.6.1.3 0 .7-.2 1L6.6 10.8z"/></svg>
        <span>+1 (555) 014-2278</span>
      </li>
      <li class="contacts__item">
        <svg class="contacts__icon" viewBox="0 0 24 24" aria-hidden="true"><path d="M2 5h20v14H2z" opacity="0.9"/><path d="M2 5l10 7 10-7" fill="none" stroke="#1e2a3c" stroke-width="1.8"/></svg>
        <span>danielmerrow@brightwave-renewables.com</span>
      </li>
      <li class="contacts__item">
        <svg class="contacts__icon" viewBox="0 0 24 24" aria-hidden="true"><path d="M12 2C8.1 2 5 5.1 5 9c0 5.2 7 13 7 13s7-7.8 7-13c0-3.9-3.1-7-7-7zm0 9.5a2.5 2.5 0 1 1 0-5 2.5 2.5 0 0 1 0 5z"/></svg>
        <span>Brightwave Renewables LLC<br>218 Harbor Lane, Boston, MA 02110</span>
      </li>
    </ul>
  </section>
</body>
</html>
```